Resume design

I am a nonprofit director looking to update my resume. My job entails positioning our organization as a leader in new communications, and I want something that reflects this - meaning it is a little crisper than what is offered by the standard resume service.
I have some examples of the type of aesthetic I'm looking for: lots of white space/breathing room, clean fonts, and a pop of color. That said, I'm not looking to create some fantastically re-envisioned version of the resume. I need to follow the general format but in a way that is elegant and sharp.
Industry/Entity Type
Communications
Requirements
Must have
- The majority of the text that I will provide (although I am open to suggestions and adjustments)
But keep to two pages. I'm open to suggestions for how to massage or shorten the text to do this.
Nice to have
- a few pops of color - esp. orange, Tiffany blue, or open to other suggestions - needs to feel fresh and cutting edge
prefer sans serif font but open to ideas
Should not have
- no photos
no artwork unless you have a suggestion for something that feels right
no tilted text
no pastel colors, and prefer to stay away from earth tones unless offset by a bolder color

```html
<!DOCTYPE html>
<html lang="en">
<head>
<meta charset="utf-8">
<title>Marisol Hart — Resume</title>
<link rel="stylesheet" href="https://fonts.googleapis.com/css2?family=Josefin+Sans:ital,wght@0,300;0,400;0,600;1,300&display=swap">
<style>
:root{
  --ink:#4a4a4a;
  --name:#6b6b6b;
  --orange:#f7941d;
  --aqua:#5ccbe0;
  --rule:#b5b5b5;
  --paper:#ffffff;
}
*{margin:0;padding:0;box-sizing:border-box}
html,body{width:927px;height:1200px;overflow:hidden;background:var(--paper)}
body{font-family:"Josefin Sans",sans-serif;color:var(--ink);font-weight:300}
.page{position:relative;width:927px;height:1200px}
.abs{position:absolute}

.name{left:52px;top:66px;font-size:68px;line-height:52px;letter-spacing:2px;color:var(--name);font-weight:300}
.contact-band{left:334px;top:128px;right:0;height:42px;background:var(--aqua);color:#fff;font-size:13.5px;font-weight:400;line-height:17px;padding:5px 0 0 12px}

.section-title{font-size:14px;font-weight:400;color:var(--orange);letter-spacing:.3px}

.summary-title{left:58px;top:232px}
.summary{left:58px;top:248px;width:286px;font-size:13.5px;line-height:17.5px;list-style:none}
.summary li{position:relative;padding-left:14px;margin-bottom:11px}
.summary li::before{content:"•";position:absolute;left:2px}

.quote{left:58px;font-size:25px;line-height:34.5px;color:var(--orange);width:292px}
.quote-one{top:624px}
.quote-two{top:888px}
.quote-by{left:58px;font-size:9.5px;line-height:12px;color:var(--ink);font-weight:400}
.quote-by-one{top:836px}
.quote-by-two{top:1068px}

.divider{left:374px;top:232px}

.career-title{left:417px;top:232px}
.org{left:417px;font-size:14px;line-height:17.5px}
.role{left:646px;font-size:14px;line-height:17.5px}
.role .years{display:block;color:var(--aqua)}

.pubs-title{left:417px;top:697px}
.pubs-intro{left:417px;top:714px;width:430px;font-size:14px;line-height:17.5px}
.pubs{left:417px;top:752px;width:500px;font-size:13.5px;line-height:17.5px;list-style:none}
.pubs li{position:relative;padding-left:14px}
.pubs li::before{content:"•";position:absolute;left:2px}
.pubs em{font-style:italic}
.pubs .note{display:block}

.leader-title{left:417px;top:992px}
.leader{left:417px;top:1009px;width:500px;font-size:14px;line-height:17.5px;list-style:none}
.leader li{margin-bottom:4px}
</style>
</head>
<body>
<main class="page">
  <h1 class="abs name">MARISOL<br>HART</h1>
  <div class="abs contact-band">58 Via Palomar | Bayhaven, California 90210 | 805-555-0147<br>marisolh@mailbox.net | www.profilehub.com/in/marisol-hart/</div>

  <svg class="abs divider" width="4" height="960" aria-hidden="true">
    <line x1="2" y1="0" x2="2" y2="960" stroke="var(--rule)" stroke-width="1.2" stroke-dasharray="2 3"/>
  </svg>

  <h2 class="abs section-title summary-title">SUMMARY</h2>
  <ul class="abs summary">
    <li>20+ years of experience with non-profit environmental organizations, currently positioned with the Harbor Bay based Coastal Green Alliance.</li>
    <li>Dedicated, results-driven manager skilled in strategic planning, team building, event planning, budget oversight, brand development and marketing.</li>
    <li>Superior communicator and environmental advocate with the ability to reach and inspire a broad audience through blogs, print publications, transformative events, and social media.</li>
    <li>Highly networked and involved community member.</li>
  </ul>

  <blockquote class="abs quote quote-one">“Marisol is the hub that makes the wheels of big projects run smoothly. Her leadership, delegation and motivational skills are exceptional.”</blockquote>
  <p class="abs quote-by quote-by-one">— Renata Vale, City Mayor</p>

  <blockquote class="abs quote quote-two">“Marisol emerged as a leader among leaders in our Bold Path program for experienced nonprofit executives.”</blockquote>
  <p class="abs quote-by quote-by-two">— Owen Marsh, President &amp; Board Chair<br>&nbsp;&nbsp;&nbsp;at Rising Together</p>

  <h2 class="abs section-title career-title">CAREER CHRONOLOGY</h2>
  <svg class="abs timeline" style="left:600px;top:248px" width="44" height="380" aria-hidden="true">
    <g stroke="var(--rule)" stroke-width="1.2" fill="none">
      <line x1="18" y1="2" x2="18" y2="374"/>
      <line x1="18" y1="16" x2="42" y2="16"/>
      <line x1="18" y1="66" x2="42" y2="66"/>
      <line x1="18" y1="116" x2="42" y2="116"/>
      <line x1="18" y1="166" x2="42" y2="166"/>
      <line x1="18" y1="236" x2="42" y2="236"/>
      <line x1="18" y1="304" x2="42" y2="304"/>
      <line x1="18" y1="372" x2="42" y2="372"/>
    </g>
  </svg>

  <p class="abs org" style="top:250px">Coastal Green Alliance,<br>Harbor Bay, CA</p>
  <p class="abs role" style="top:256px"><span class="years">2006 - Present</span>Assistant Director</p>
  <p class="abs role" style="top:306px"><span class="years">2004 - 2006</span>Community Relations Director</p>
  <p class="abs role" style="top:356px"><span class="years">1996 - 2004</span>Communications Director</p>
  <p class="abs role" style="top:406px"><span class="years">1995 - 1996</span>Communications Associate</p>

  <p class="abs org" style="top:476px">Tidewater Living<br>Magazine, Harbor Bay, CA</p>
  <p class="abs role" style="top:476px"><span class="years">2011 - Present</span>Sustainability Editor</p>

  <p class="abs org" style="top:544px">Council for Efficient Power,<br>Washington, D.C.</p>
  <p class="abs role" style="top:544px"><span class="years">1993 - 1995</span>Communications Associate</p>

  <p class="abs org" style="top:612px">National Habitat<br>League, Washington, D.C.</p>
  <p class="abs role" style="top:612px"><span class="years">1992 - 1993</span>Communications Assistant</p>

  <h2 class="abs section-title pubs-title">SAMPLE PUBLICATIONS</h2>
  <p class="abs pubs-intro">Author and/or editor of dozens of technical reports and advocacy papers, including:</p>
  <ul class="abs pubs">
    <li><em>A Fresh Power Course: A Roadmap for Harbor Bay County,</em><span class="note">http://www.cgalliance.org/publications (strategy report)</span></li>
    <li><em>Does Our State Need Imported Natural Gas?</em><span class="note">http://www.cgalliance.org/publications (policy paper)</span></li>
    <li><em>Sunlight Power in Harbor Bay County: the Next Steps for Clearing Obstacles,</em><span class="note">http://www.cgalliance.org/publications (strategy report)</span></li>
    <li><em>CleanStart for Children</em> (survey brief and final report)</li>
    <li><em>Recovery Methods and Resource Handling in the Modern Century</em><span class="note">(technical paper)</span></li>
    <li><em>Rethinking Solid Waste As We Know It: Handling Resources in a New Century</em><span class="note">(policy paper)</span></li>
  </ul>

  <h2 class="abs section-title leader-title">COMMUNITY LEADERSHIP</h2>
  <ul class="abs leader">
    <li>Board Member, (2013-Present), Rising Together, Harbor Bay, CA</li>
    <li>Alumni Committee Chair, (2011-Present), Bold Path, Harbor Bay, CA</li>
    <li>Participant (2009-2010), Bold Path, Harbor Bay, CA</li>
    <li>Planning Committee Member, (2009-2012), Alliance for Nonprofit Quality,<br>Harbor Bay, CA</li>
    <li>Participant, (2011), Pacific Social Impact Review: Non-Profit Management Institute, Harbor Bay, CA</li>
  </ul>
</main>
</body>
</html>
```